7 ¾ long by 5 inches high print ad

I have a 1/2 page ad for a print magazine I need to be designed. Uploaded is the previous year design. We want something to be more aligned with our new website look/feel and new messaging from website.

I have provided some photos, the logo, color codes and a recent banner ad sample for copy.

Target Market(s)

Developers

Font styles to use
Sans Serif

Requirements
Must have
• Clear headline, sub headline, and value statement
• Services to highlight, Tilt-Up Construction,
• Website, phone, social icons, Facebook, Twitter, and LinkedIn
Nice to have
• https://marrowcrestbuilding.com/
• Some of the logos in the clients who trust us section

```html
<!DOCTYPE html>
<html lang="en">
<head>
<meta charset="utf-8">
<title>Marrowcrest Construction – Never Compromise</title>
<link rel="stylesheet" href="https://fonts.googleapis.com/css2?family=Montserrat:wght@500;600;700;900&family=Raleway:wght@400;500;600&family=Barlow+Semi+Condensed:wght@400;500&display=swap">
<style>
:root{
  --orange:#ef7d23;
  --orange-light:#f39a2b;
  --amber:#eea02f;
  --plum:#6b3f6a;
  --navy:#1c2448;
  --navy-deep:#131833;
  --white:#ffffff;
  --ink:#3a3a3a;
  --page:#e6e6e6;
}
*{box-sizing:border-box;margin:0;padding:0}
html,body{width:1200px;height:949px;overflow:hidden;background:var(--page)}
.ad{position:absolute;left:0;top:31px;width:1200px;height:886px;overflow:hidden;background:var(--navy);font-family:"Montserrat",sans-serif}
.photo{position:absolute;left:0;top:82px;width:1200px;height:804px;
  background:linear-gradient(160deg,#5d6d86 0%,#7f95ad 30%,#4b5a74 55%,#6a4e52 75%,#2f3550 100%)}
.photo-shade{position:absolute;left:0;top:466px;width:560px;height:420px;
  background:linear-gradient(90deg,rgba(19,24,51,.95) 0%,rgba(28,36,72,.8) 60%,rgba(28,36,72,0) 100%)}
.headline-wash{position:absolute;left:365px;top:82px;width:835px;height:307px;
  background:linear-gradient(90deg,var(--amber) 0%,rgba(238,160,47,.92) 40%,rgba(200,110,50,.55) 75%,rgba(120,60,60,.35) 100%)}
.tagbar{position:absolute;left:365px;top:0;width:835px;height:70px;background:var(--white);
  display:flex;align-items:center;justify-content:center;gap:18px;font-family:"Raleway",sans-serif;font-size:30px;font-weight:500;letter-spacing:.5px}
.tagbar .accent{color:var(--orange)}
.tagbar .muted{color:var(--ink)}
.tagbar .sep{color:var(--orange);font-weight:400}
.tagrule{position:absolute;left:365px;top:70px;width:835px;height:12px;background:var(--orange)}
.headline{position:absolute;left:400px;top:108px;color:var(--white);font-weight:900;line-height:1;letter-spacing:-4px}
.headline .l1{display:block;font-size:118px}
.headline .l2{display:block;font-size:104px;margin-top:30px;letter-spacing:-4px}
.side{position:absolute;left:0;top:0;width:365px;height:466px;
  background:linear-gradient(180deg,var(--orange-light) 0%,var(--orange) 45%,#c8663e 80%,#8e4a58 100%)}
.brand{position:absolute;left:24px;top:18px;display:flex;align-items:center;gap:14px;color:var(--white);font-weight:500}
.brand-mark{width:50px;height:50px;background:var(--white)}
.brand-name{font-size:28px;line-height:1}
.brand-name small{display:block;font-size:18px;margin-top:4px}
.promise-box{position:absolute;left:29px;top:119px;width:302px;height:198px;border:2px solid rgba(255,255,255,.85);
  padding:12px 0 0 12px;color:var(--white);font-family:"Raleway",sans-serif;font-weight:600;font-size:29px;line-height:44px;letter-spacing:1px}
.promise-box .lead{color:var(--navy);font-weight:400;font-size:40px}
.promise-box .lead-rest{font-weight:400}
.promise-box .tight{font-size:27px;letter-spacing:0}
.thats{position:absolute;left:0;width:365px;top:322px;text-align:center;color:var(--white);font-family:"Raleway",sans-serif;font-weight:500;font-size:38px;letter-spacing:1px}
.promise-band{position:absolute;left:0;top:388px;width:365px;height:59px;background:rgba(60,40,60,.55);
  color:var(--white);font-weight:700;font-size:37px;letter-spacing:7px;display:flex;align-items:center;justify-content:center}
.services{position:absolute;left:0;top:0;width:560px;height:886px}
.service-spine{position:absolute;left:57px;top:520px;width:2px;height:310px;background:var(--white)}
.service{position:absolute;left:18px;width:492px;height:70px}
.service-pill{position:absolute;left:40px;top:0;right:0;height:70px;border:2px solid var(--white);border-left:none;border-radius:0 36px 36px 0;
  background:linear-gradient(90deg,rgba(70,45,90,.9) 0%,#b35a4e 55%,var(--orange) 100%);
  display:flex;align-items:center;padding-left:64px;color:var(--white);font-weight:600;font-size:23px;line-height:1.2;letter-spacing:.3px}
.service-icon{position:absolute;left:0;top:-4px;width:78px;height:78px;border-radius:50%;background:var(--navy);
  border:2px solid var(--white);box-shadow:0 0 0 4px var(--navy);display:flex;align-items:center;justify-content:center}
.footer{position:absolute;left:520px;top:808px;width:680px;height:78px;
  background:linear-gradient(90deg,rgba(100,55,95,.9) 0%,#b5594c 55%,var(--orange) 100%);
  border-top:2px solid rgba(255,255,255,.7);border-top-left-radius:40px;
  color:var(--white);font-family:"Barlow Semi Condensed",sans-serif;font-size:17px}
.contact{position:absolute;left:64px;top:14px;line-height:26px}
.contact span{display:flex;align-items:center;gap:10px}
.projects{position:absolute;right:38px;top:14px;text-align:right;line-height:26px}
.projects strong{font-weight:500;font-size:18px}
</style>
</head>
<body>
<div class="ad">
  <div class="photo" role="img" aria-label="Photo of modern glass office buildings with a construction crane and a street in front"></div>
  <div class="photo-shade"></div>
  <div class="headline-wash"></div>

  <div class="tagbar">
    <span class="accent">YOUR BUILDING</span><span class="sep">|</span>
    <span class="muted">YOUR SCHEDULE</span><span class="sep">|</span>
    <span class="accent">OUR SKILLS</span>
  </div>
  <div class="tagrule"></div>

  <h1 class="headline"><span class="l1">NEVER</span><span class="l2">COMPROMISE</span></h1>

  <div class="side">
    <div class="brand">
      <div class="brand-mark"></div>
      <div class="brand-name">Marrowcrest<small>Construction, Inc.</small></div>
    </div>
    <p class="promise-box">
      <span class="lead">YOUR</span> <span class="lead-rest">PROJECT</span><br>
      SHOULD NEVER<br>
      SACRIFICE TIME,<br>
      <span class="tight">QUALITY, OR PRICE.</span>
    </p>
    <p class="thats">THAT'S OUR</p>
    <p class="promise-band">PROMISE</p>
  </div>

  <div class="services">
    <div class="service-spine"></div>
    <div class="service" style="top:481px">
      <div class="service-pill">CONSTRUCTION CONSULTING<br>AND PLANNING</div>
      <div class="service-icon">
        <svg width="38" height="38" viewBox="0 0 38 38" fill="none" stroke="#fff" stroke-width="3"><rect x="6" y="4" width="18" height="24"/><rect x="14" y="12" width="18" height="22" fill="#1c2448"/></svg>
      </div>
    </div>
    <div class="service" style="top:585px">
      <div class="service-pill">GENERAL<br>CONTRACTING</div>
      <div class="service-icon">
        <svg width="30" height="38" viewBox="0 0 30 38"><rect x="2" y="2" width="26" height="34" fill="#fff"/><g fill="#1c2448"><rect x="7" y="7" width="4" height="4"/><rect x="13" y="7" width="4" height="4"/><rect x="19" y="7" width="4" height="4"/><rect x="7" y="14" width="4" height="4"/><rect x="13" y="14" width="4" height="4"/><rect x="19" y="14" width="4" height="4"/><rect x="7" y="21" width="4" height="4"/><rect x="13" y="21" width="4" height="4"/><rect x="19" y="21" width="4" height="4"/><rect x="12" y="28" width="6" height="8"/></g></svg>
      </div>
    </div>
    <div class="service" style="top:689px">
      <div class="service-pill">MAINTENANCE<br>BUILDING/PROPERTY</div>
      <div class="service-icon">
        <svg width="40" height="36" viewBox="0 0 40 36" fill="#fff"><circle cx="14" cy="20" r="9"/><circle cx="14" cy="20" r="4" fill="#1c2448"/><g stroke="#fff" stroke-width="4"><line x1="14" y1="7" x2="14" y2="33"/><line x1="1" y1="20" x2="27" y2="20"/><line x1="5" y1="11" x2="23" y2="29"/><line x1="23" y1="11" x2="5" y2="29"/></g><circle cx="14" cy="20" r="4" fill="#1c2448"/><circle cx="31" cy="9" r="6"/><circle cx="31" cy="9" r="2.5" fill="#1c2448"/><circle cx="31" cy="28" r="5"/><circle cx="31" cy="28" r="2" fill="#1c2448"/></svg>
      </div>
    </div>
    <div class="service" style="top:793px">
      <div class="service-pill">TILT-UP CONSTRUCTION</div>
      <div class="service-icon">
        <svg width="34" height="36" viewBox="0 0 34 36"><polygon points="4,8 16,3 30,8 30,30 18,34 4,29" fill="#fff"/><polygon points="16,12 30,8 30,30 18,34" fill="#c9ccd8"/></svg>
      </div>
    </div>
  </div>

  <div class="footer">
    <div class="contact">
      <span><svg width="12" height="14" viewBox="0 0 12 14" fill="#fff"><path d="M2 1l3 0 1 3-2 1.5c.8 2 2 3.2 3.5 4L9 7.5l3 1v3c0 1-1 1.5-2 1.5C5 12.5 .5 8 .5 2.5 .5 1.5 1 1 2 1z"/></svg>916.555.0142</span>
      <span><svg width="12" height="16" viewBox="0 0 12 16" fill="#fff"><path d="M6 0C2.7 0 0 2.6 0 5.8 0 10 6 16 6 16s6-6 6-10.2C12 2.6 9.3 0 6 0zm0 8.2a2.4 2.4 0 110-4.8 2.4 2.4 0 010 4.8z"/></svg>2280 Ridgeline Ave., Suite 4 Sacramento, CA 95815</span>
    </div>
    <div class="projects">View our projects:<br><strong>marrowcrestbuilding.com</strong></div>
  </div>
</div>
</body>
</html>
```